Business card for a young woman who performs life enhancement activities with people who have developmental disabilities, what used to be called retardation. She wants to focus on the creative part of her work. She has a degree in art and will engage clients in art projects as well as helping them learn to do things like grocery shop, cook meals, set goals, and live independently.

Target Market(s)

Parents, caregivers, guardians, relatives of people with developmental disabilities, meaning they have not developed in their mental capacities.

Industry/Entity Type

Business

Contact Information for Business Card

Bright Path Care Studio, Marisa J. Tolliver, 417 263-9184, marisa@marisatolliver.example, Life enhancement services for people with developmental disabilities. No address.

Font styles to use
Serif

Requirements
Must have
• Marisa wants it to have some indication of the art or creative part of her work with clients. But it must also be businesslike so it appeals to the parents. They have to see her as a professional, but she's compassionate and artsy. She wants just her company name on the front. The other information should be on the back.

```html
<!DOCTYPE html>
<html lang="en">
<head>
<meta charset="utf-8">
<title>Bright Path Care Studio – Business Card</title>
<link rel="stylesheet" href="https://fonts.googleapis.com/css2?family=Playfair+Display:wght@400&family=Lora:wght@400;500&display=swap">
<style>
  :root {
    --page: #dcdcdc;
    --white: #ffffff;
    --ink: #161210;
    --bar: #e6911f;
    --bar-icon: #f6b53a;
    --accent: #7b3f9e;
    --photo-warm: #c98a56;
    --photo-soft: #e9b06a;
    --photo-faded: #e6a557;
  }
  * { box-sizing: border-box; margin: 0; padding: 0; }
  html, body { width: 1200px; height: 1000px; overflow: hidden; }
  body { background: var(--page); position: relative; font-family: "Lora", Georgia, serif; }

  .card { position: absolute; overflow: hidden; }
  .card-back-side { left: 275px; top: 88px; width: 658px; height: 384px; }
  .card-front-side { left: 271px; top: 510px; width: 665px; height: 388px; }
  .card-art { position: absolute; inset: 0; width: 100%; height: 100%; }

  .brand {
    position: absolute;
    display: flex;
    align-items: center;
    justify-content: center;
    gap: 12px;
  }
  .brand-dot {
    flex: none;
    width: 16px; height: 16px;
    border-radius: 50%;
    background: var(--accent);
  }
  .brand-name {
    font-family: "Playfair Display", Georgia, serif;
    font-weight: 400;
    color: var(--ink);
    line-height: 1.12;
    text-align: center;
    letter-spacing: 0.3px;
  }
  .card-back-side .brand { left: 350px; top: 94px; width: 270px; }
  .card-back-side .brand-name { font-size: 28px; }
  .card-front-side .brand { left: 329px; top: 136px; width: 300px; }
  .card-front-side .brand-name { font-size: 31px; }

  .tagline {
    position: absolute;
    right: 36px; top: 202px;
    font-size: 12px;
    font-weight: 500;
    line-height: 23px;
    text-align: right;
    color: var(--ink);
    text-transform: uppercase;
    letter-spacing: 0.3px;
  }

  .contact-list { position: absolute; left: 370px; top: 260px; width: 256px; list-style: none; }
  .contact-row {
    position: relative;
    height: 25px;
    margin-bottom: 12px;
    background: linear-gradient(90deg, #f4ab1e, var(--bar) 40%, #de8a22);
    color: var(--white);
    font-size: 13.5px;
    line-height: 25px;
    text-align: right;
    padding-right: 9px;
    white-space: nowrap;
  }
  .contact-row:nth-child(3) { margin-top: -4px; font-size: 12.5px; }
  .contact-icon {
    position: absolute; left: 0; top: 0;
    width: 35px; height: 25px;
    background: var(--bar-icon);
  }
  .contact-icon svg { position: absolute; left: 7px; top: 2px; width: 21px; height: 21px; }
</style>
</head>
<body>

  <!-- Information side -->
  <section class="card card-back-side" aria-label="Business card, contact side">
    <svg class="card-art" viewBox="0 0 658 384">
      <defs>
        <linearGradient id="info-bg" x1="0" y1="0" x2="1" y2="0.3">
          <stop offset="0" stop-color="#dc8420"/>
          <stop offset="1" stop-color="#e8951f"/>
        </linearGradient>
        <radialGradient id="info-glow" cx="0.75" cy="0.2" r="0.7">
          <stop offset="0" stop-color="#f5b41f"/>
          <stop offset="1" stop-color="#ee9d21"/>
        </radialGradient>
        <radialGradient id="photo-tone" cx="0.55" cy="0.4" r="0.65">
          <stop offset="0" stop-color="var(--photo-soft)"/>
          <stop offset="1" stop-color="var(--photo-warm)"/>
        </radialGradient>
      </defs>
      <rect width="658" height="384" fill="url(#info-bg)"/>
      <path d="M390 0 C 470 90, 400 300, 330 384 L658 384 L658 0 Z" fill="url(#info-glow)"/>
      <circle cx="140" cy="207" r="166" fill="var(--white)"/>
      <circle cx="140" cy="207" r="148" fill="url(#photo-tone)" role="img" aria-label="Photo of the caregiver smiling with a client"/>
      <circle cx="218" cy="10" r="22" fill="none" stroke="var(--white)" stroke-width="9"/>
      <circle cx="303" cy="48" r="46" fill="none" stroke="var(--white)" stroke-width="12"/>
      <circle cx="322" cy="132" r="24" fill="none" stroke="var(--white)" stroke-width="9"/>
    </svg>

    <div class="brand">
      <span class="brand-dot"></span>
      <p class="brand-name">Bright Path<br>Care Studio</p>
    </div>

    <p class="tagline">Life enhancement services for people<br>with developmental disabilities.</p>

    <ul class="contact-list">
      <li class="contact-row">
        <span class="contact-icon"><svg viewBox="0 0 21 21"><circle cx="10.5" cy="4" r="3" fill="#fff"/><path d="M6 9h9v6h-2v5h-5v-5H6z" fill="#fff"/></svg></span>
        Marisa J. Tolliver
      </li>
      <li class="contact-row">
        <span class="contact-icon"><svg viewBox="0 0 21 21"><rect x="3" y="2" width="15" height="17" rx="2" fill="#fff"/><path d="M8 5c-1 1-1 4 1 7s4 4 5 3l-1.5-2-1.5.7c-1-1-2-2.5-2.3-3.8l1.3-1L9 5z" fill="var(--bar-icon)"/></svg></span>
        417 263-9184
      </li>
      <li class="contact-row">
        <span class="contact-icon"><svg viewBox="0 0 21 21"><rect x="1.5" y="4.5" width="18" height="12" fill="none" stroke="#fff" stroke-width="1.3"/><path d="M1.5 4.5l9 7 9-7M1.5 16.5l6.5-6M19.5 16.5l-6.5-6" fill="none" stroke="#fff" stroke-width="1.3"/></svg></span>
        marisa@marisatolliver.example
      </li>
    </ul>
  </section>

  <!-- Company name side -->
  <section class="card card-front-side" aria-label="Business card, company name side">
    <svg class="card-art" viewBox="0 0 665 388">
      <defs>
        <linearGradient id="front-bg" x1="0" y1="0" x2="1" y2="0">
          <stop offset="0" stop-color="#dc8520"/>
          <stop offset="1" stop-color="#eea022"/>
        </linearGradient>
        <radialGradient id="faded-photo" cx="0.5" cy="0.45" r="0.6">
          <stop offset="0" stop-color="#efb569"/>
          <stop offset="1" stop-color="var(--photo-faded)"/>
        </radialGradient>
      </defs>
      <rect width="665" height="388" fill="url(#front-bg)"/>
      <path d="M330 0 C 420 80, 420 300, 300 388 L665 388 L665 0 Z" fill="#f2a61f"/>
      <circle cx="180" cy="175" r="222" fill="url(#faded-photo)" role="img" aria-label="Faded photo of the caregiver and a client"/>
      <circle cx="479" cy="172" r="167" fill="var(--white)"/>
      <circle cx="283" cy="205" r="25" fill="none" stroke="var(--white)" stroke-width="9"/>
      <circle cx="266" cy="298" r="55" fill="none" stroke="var(--white)" stroke-width="13"/>
    </svg>

    <div class="brand">
      <span class="brand-dot"></span>
      <p class="brand-name">Bright Path<br>Care Studio</p>
    </div>
  </section>

</body>
</html>
```